8.5 x 11 Two Sided Flyer with our coffee descriptions/images

See www.WillowmereCoffee.com for elements and design look.

I have need to put all of our coffee bags onto a flyer with a brief description of each.

The header title should have the logo and the words Willowmere Coffee Co.
Underneath a paragraph that states:
Located in the hills of Renwick County, Georgia, our small-batch craft coffees are freshly-roasted from responsibly sourced beans to ensure premium quality and taste. Retail: $19.95 for a full 16 oz. pound of freshly roasted ground or whole bean coffee. Wake up to better coffee with Willowmere Coffee!

Then below, a small image of each of the coffees with their descriptions. SEE THE BOTTOM OF THIS PROJECT DESCRIPTION

At the very bottom, the url - www.WillowmereCoffee.com

The coffees should remain in the order provided.

SOLE PIENO - Italian Roast
Hints of Dark Chocolate and Raspberry

From the hillsides of Tuscany to the waters of the Amalfi coast to the architecture of Rome, Italy is one of the most beautiful countries in the world.

Whether it’s high fashion and fast cars or fine wine an extra-virgin olive oil, the word “Italian” is synonymous with quality and the enjoyment of life’s finer things. As an old Italian proverb urges, “If you cannot live longer, live deeper.”

Following in the footsteps of his great-grandfather Enzo, Marcus Delvecchi is a second generation Italian-American entrepreneur with a passion for living life to the fullest. A successful businessman, Enzo had a steel-like work ethic that fueled his vision. He saw opportunity, and through hard work and determination, would soon see it thrive. Volumes could be written about all that Italians like Enzo have contributed to the world.

When you walk the streets of Italy, you’ll also discover that Italians know no strangers. If you take the opportunity to visit one of the many cafes in any Italian city, you’ll be greeted with warm and sincere hospitality. “Sole Pieno!” You’ll be offered gelato, a cannoli, likely a robust cup of caffé. Italians love their coffee almost as much as their wine. By the time you regretfully move on, you will be among friends.

To this end, we proclaim “Sole Pieno,” and invite you to take a moment to live deeply and enjoy this robust Italian roast with us, your new friends, before you tackle life’s newest adventure.

Ciao.

ARCADIA - 4 X Caffeine - Sumatran & Indian

Arcadia: The afterlife where the chosen, the righteous, and the heroic indulge in everlasting pleasure. Compare to Grave Dare coffee.

This propriety blend is shown to possess more than four times the caffeine content of your standard cup. Experience the divinely bold coffee cup that results from exotic, dark-roasted Sumatran and Indian beans, where earthy notes and mild acidity balance to produce a rich, heavy body.

Why wish for death when you can experience Arcadia?

KEYSTONE - Medium-Dark Roast Blend - Africa & Central America
Bold and hearty with notes of cocoa

Keystone Blend celebrates the “melting pot” quality that gives our United States vitality.

The Keystone Blend is intentionally mixed and roasted to be bold, the way we’d like all coffee to be. It begins with a refreshing balance of the best beans from Central America and Africa, and ends with a flavor only roasting in America can provide.

The specific flavors of this blend will vary from season to season, as all good coffees do, with coffee farming and cultivation ever changing throughout the year. But the essence of American craftsmanship will always ring true in this blended roast.

We wanted a coffee dedicated to American ideals. We wanted a drink worthy of our Founding Fathers; a drink we’d gladly brew in the great American tradition of consuming coffee—going all the way back to the Boston Tea Party.
After countless roasting sessions and tasting cup after cup of coffee, we settled on a combination of medium-dark roasted and dark roasted beans (we suspect James Madison made his the same way). The resulting blend is technically known as a melange, but we still call it a blend; one in keeping with the diverse and blended nature of our favorite constitutional republic.

DRIFTER - Decaf Medium-Dark Roast - Guatemala
Herbal and sweet with notes of caramel

Wind down with our fragrant and luscious decaf. Its complex aroma and smooth, sweet taste are a great way to start your decaffeinated day. Pairs well with chocolate or sugar cookies. Try it iced with your favorite syrup and whipped cream for a decadent, soothing indulgence.

Sleep easy knowing Drifter is always Alpine Brook Processed and never chemically decaffeinated.

RANCHLAND - Medium Roast - Ethiopia
Bright and vibrant with notes of blueberry

The first Ranchland Act of 1862 gave plots of land to farmers in the federally-owned properties of the West. The kinds of people who took advantage of this offer had a unique combination of traits.

On one hand, they were adventurous enough to leave the “settled” lands and move to the frontier. On the other hand, these were people looking for homes. They wanted to settle down, start families, and send down deep roots.

The Ranchland Roast honors that curious combination of traits. It’s a member of the Willowmere Coffee family, so you know it’s not going to be the coffee-as-usual you might expect from other roasters. It’s dauntless in that way.

But it’s also comfortable and cordial. The Ranchland Roast just might put the word “hearth” in mind. Or “front porch.” That works too.

Vibrant and spirited, with citrus acidity and a smooth finish, the Ranchland Roast is deliciously versatile. It wakes you up in the morning and facilitates your after-dinner conversation.

Ranchland Roast brews up a golden brown, but it’s not overpowering. In fact, you might call it hospitable, because it always makes room for sugar and cream – or flavored syrup, if that’s your thing.

Even if you prefer a darker roast for yourself, the Ranchland Roast makes a great addition to your home or business pantry to ensure you always have a satisfying, rich cup of coffee right in the comfort zone of most coffee drinkers.

WAYFARER - Medium-Dark Roast - Bolivia
Sweet and citric with notes of almond

America has always had more than its fair share of pioneers. From Daniel Boone to Jimi Hendrix to Steve Jobs, there’s something in our DNA that drives us to do things a little differently.

But pioneers are nothing if not practical. Because a useless innovation is in many ways worse than a mediocre commonplace.

That’s why we named our medium-dark roast the Wayfarer. It’s bold, for sure. But it’s not brash. It’s for the pioneer in all of us—with one eye on the frontier, and the other on taking care of business.

Velvety and rich, with notes of tree nuts and cocoa, the versatile Wayfarer Roast strikes out into the unexplored territory of the bold roast profiles.

The medium-dark Wayfarer Roast plays double duty. A “Goldilocks” blend that’s not too dark or too light, its flexible flavor profile goes well with foods both savory and sweet.

If you opt for fried bacon and scrambled eggs for breakfast over a bowl of cold cereal or a bagel, you’ll find the Wayfarer Roast’s notes of earthiness and toasted grain pleasantly accent your rich, savory breakfast.

On the other fork, if you’re looking for a good coffee to drink with your decadent double-decker chocolate cake, you’ll find Wayfarer Roast’s touch of smokiness cuts through and complements your sugary treat.

BONANZA - Dark Roast - Burundi
Chocolatey with notes of cherry

American prospectors made it all the way to the coast. They were never able to shake that pilgrim feeling that there was something even better a little further West… just a bit further on.

When some settlers hunkered down and built houses in the fly-over states, the prospectors kept going. They were looking for gold. But they were really hoping for a dream.

The Bonanza Roast honors that tradition. Going well beyond first crack, our expert roasters take these intrepid beans all the way to oil-coated glory. This is a bean that goes the distance. For people who won’t settle for anything less.

This dark-roasted bean packs a serious punch. Not all beans can stand up to the intense roasting temperatures required to turn a green bean into a lean, mean, caffeine machine.

That’s why our single origin Bonanza Roast utilizes only the most robust beans from the mountains of Central Africa to give you the maximum in bean and roast flavor in one compact package.

But let’s face it. You’re drinking this coffee because you like the complexity and richness that only a dark bean can offer. Sure, this coffee will pair with food. But who cares? This is a coffee you drink on its own. You drink it black.

You listen to music. You light your pipe, your cigar, your fire. This will keep you going. No matter what your prospects.

OUTPOST - Medium-Dark Roast - India, Ethiopia, Brazil
Hearty and nutty with a berry finish

Saddle up with a savory, complex and decadent roast. Perfect for all your favorite espresso drinks! Outpost can also be prepared without an espresso machine. Explore the expansive flavor profile with your preferred brewing method.

Outpost is blended with the finest beans from India, Ethiopia and Brazil. This espresso offers a hearty mouthfeel with a sweet berry finish.

DEAN MORROW’S RIPTIDE - Dark Roast - Brazil, Sumatra, Kenya

“This dark roast is what is I crave from a cup of coffee. Big, full-bodied, and bold. My exotic blend is made from responsibly sourced Brazilian, Sumatran and Kenyan beans. This coffee is the perfect way to embrace a beautiful day. Mahalo!” – Dean Morrow

DEAN MORROW’S ROCKET - Medium 2X Caffeine - Sumatra, India
“Rocket is my nickname, because I go fast and head first into what I love. It takes a special coffee to tackle the biggest waves. Be warned this coffee has more than double the caffeine of your standard cup. Responsibly sourced Sumatran & Indian beans bring balance to the scales of flavor and power. This coffee is the perfect way to tackle an epic day. Shoots!” – Dean Morrow

Target Market(s)

Grocery buyers

Industry/Entity Type

Grocery

Font styles to use
Serif
Sans Serif

Requirements
Must have
• Uniformity in the size and font styles - pretend it's a catalog
Nice to have
• Elements of brown / gold / black
Should not have
• Do not use bright colors - this is a luxury market and coffee related, does not want bright or neon colors

```html
<!DOCTYPE html>
<html lang="en">
<head>
<meta charset="utf-8">
<title>Willowmere Coffee Co. — Sole Pieno</title>
<link href="https://fonts.googleapis.com/css2?family=Lusitana:wght@400;700&display=swap" rel="stylesheet">
<style>
  :root {
    --backdrop: #e6e6e6;
    --paper: #ecdcbf;
    --paper-edge: #e3d0ae;
    --ink: #1f1a14;
    --rust: #8d3a22;
    --cream: #f7ecd9;
    --gold: #b5772e;
    --wood-dark: #3a2c22;
    --wood-mid: #6a5646;
    --bird-brown: #a4622e;
  }
  * { box-sizing: border-box; margin: 0; padding: 0; }
  html, body { width: 900px; height: 1200px; overflow: hidden; background: var(--backdrop); }
  body { position: relative; font-family: "Lusitana", Georgia, serif; color: var(--ink); }

  .flyer {
    position: absolute; left: 33px; top: 38px; width: 833px; height: 1080px;
    background: linear-gradient(180deg, var(--paper), var(--paper-edge));
    box-shadow: 3px 4px 6px rgba(0,0,0,.25);
    overflow: hidden;
  }

  .brand {
    position: absolute; left: 42px; top: 46px; width: 380px;
    display: flex; align-items: center; gap: 18px;
  }
  .brand-dot { flex: none; width: 84px; height: 84px; border-radius: 50%; background: var(--ink); }
  .brand-name { font-weight: 700; font-size: 40px; line-height: 40px; color: var(--ink); }

  .intro {
    position: absolute; left: 454px; top: 0; width: 356px; height: 225px;
    background: var(--rust); border-radius: 0 0 0 12px;
    padding: 38px 24px 0 26px;
    color: var(--cream); font-size: 15.5px; line-height: 20px;
  }
  .intro b { font-weight: 700; }

  .bag {
    position: absolute; left: 44px; top: 257px; width: 170px; height: 377px;
    background: linear-gradient(160deg, #5b4436, #3b2b22 70%, #2e221b);
    border-radius: 4px 4px 2px 2px;
  }

  .coffee {
    position: absolute; left: 264px; top: 260px; width: 520px;
    font-size: 13.2px; line-height: 16.6px; text-align: justify;
  }
  .coffee p { margin-bottom: 16.6px; }
  .coffee-title { font-weight: 700; text-align: left; }

  .url {
    position: absolute; right: 50px; top: 852px; font-weight: 700; font-size: 13px;
  }
  .rule { position: absolute; left: 240px; right: 0; top: 875px; height: 8px; background: var(--gold); }
  .wood {
    position: absolute; left: 287px; right: 0; top: 883px; bottom: 0;
    background: linear-gradient(90deg, var(--wood-mid), var(--wood-dark) 40%, #4b3a2d 75%, var(--wood-dark));
    display: flex; align-items: center; justify-content: center;
  }
  .wood-name {
    font-weight: 700; font-size: 44px; line-height: 46px; color: var(--cream);
    opacity: .85; text-align: center; max-width: 460px;
  }
  .mascot {
    position: absolute; left: 0; top: 792px; width: 287px; height: 288px;
    background: radial-gradient(circle at 40% 45%, #c0854a, var(--bird-brown) 55%, #6b3e1e);
  }
</style>
</head>
<body>
  <main class="flyer">
    <header class="brand">
      <span class="brand-dot"></span>
      <span class="brand-name">Willowmere<br>Coffee Co.</span>
    </header>

    <section class="intro">
      Located in the hills of <b>Renwick County, Georgia</b>, our small-batch craft coffees are <b>freshly-roasted</b> from responsibly sourced beans to ensure <b>premium quality &amp; taste</b>. <b>Retail: $19.95</b> for a full 16 oz. pound of <b>freshly roasted ground</b> or <b>whole bean coffee</b>. Wake up to better coffee with <b>Willowmere Coffee!</b>
    </section>

    <div class="bag" role="img" aria-label="Sole Pieno Italian Roast coffee bag, brown package with portrait label and Italian flag"></div>

    <article class="coffee">
      <p class="coffee-title">SOLE PIENO - Italian Roast</p>
      <p>Hints of Dark Chocolate and Raspberry</p>
      <p>From the hillsides of Tuscany to the waters of the Amalfi coast to the architecture of Rome, Italy is one of the most beautiful countries in the world.</p>
      <p>Whether it’s high fashion and fast cars or fine wine an extra-virgin olive oil, the word “Italian” is synonymous with quality and the enjoyment of life’s finer things. As an old Italian proverb urges, “If you cannot live longer, live deeper.”</p>
      <p>Following in the footsteps of his great-grandfather Enzo, Marcus Delvecchi is a second generation Italian-American entrepreneur with a passion for living life to the fullest. A successful businessman, Enzo had a steel-like work ethic that fueled his vision. He saw opportunity, and through hard work and determination, would soon see it thrive. Volumes could be written about all that Italians like Enzo have contributed to the world.</p>
      <p>When you walk the streets of Italy, you’ll also discover that Italians know no strangers. If you take the opportunity to visit one of the many cafes in any Italian city, you’ll be greeted with warm and sincere hospitality. “Sole Pieno!” You’ll be offered gelato, a cannoli, likely a robust cup of caffé. Italians love their coffee almost as much as their wine. By the time you regretfully move on, you will be among friends.</p>
      <p>To this end, we proclaim “Sole Pieno,” and invite you to take a moment to live deeply and enjoy this robust Italian roast with us, your new friends, before you tackle life’s newest adventure.</p>
      <p>Ciao.</p>
    </article>

    <div class="url">www.WillowmereCoffee.com</div>
    <div class="rule"></div>
    <div class="wood" role="img" aria-label="Weathered wood plank texture with the company name painted on it">
      <span class="wood-name">Willowmere<br>Coffee Co.</span>
    </div>
    <div class="mascot" role="img" aria-label="Large brown bird mascot illustration"></div>
  </main>
</body>
</html>
```